Forensic Document Examiner, looking for contemporary update to my stationery design.

Looking for professional, classy logo design for stationery and business cards. My current stationery and business card is attached.I believe a logo image makes a header section interesting, so an intriguing design of a pen, feathered pen, microscope, magnifying glass, etc., would be appropriate. I have been in the business for over 30 years. I leave ideas to the imagination of the designer.My work involves mainly, the comparison of signatures and handwriting. I also resolve alterations, obliterations, and work as shown on my website: www.documentexaminer.infoThe image produced will be printed on quality white stationery and envelopes. The stationery will be photocopied by my clients, so the images should be reproducible. The business cards may be designed in other than white.

Target Market(s)

Attorneys

Font styles to use
Sans Serif

Colors

Designer to choose colors to be used in the design.

Requirements
Must have
• Image suitable for white stationery and photocopying.
• Classy logo and image; no casual fonts.
Nice to have
• Intriguing, contemporary design incorporating a relevant logo to my work.

```html
<!DOCTYPE html>
<html lang="en">
<head>
<meta charset="utf-8">
<title>Marian T. Holloway – Stationery</title>
<link rel="stylesheet" href="https://fonts.googleapis.com/css2?family=Questrial&family=Open+Sans:wght@400;600&display=swap">
<style>
  :root {
    --backdrop: #dcdcdc;
    --paper: #f7f7f7;
    --brand-blue: #33309a;
    --brand-gold: #e2ab0c;
    --ink: #555555;
    --ink-dark: #333333;
    --fold: #e6e6e6;
  }
  * { box-sizing: border-box; margin: 0; padding: 0; }
  html, body { width: 1200px; height: 877px; overflow: hidden; background: var(--backdrop); }
  body { position: relative; font-family: "Questrial", sans-serif; color: var(--ink); }

  .sheet { position: absolute; background: var(--paper); box-shadow: 0 1px 3px rgba(0,0,0,.12); }
  .footer-band {
    position: absolute; left: 0; right: 0; height: 17px; background: var(--brand-blue);
    color: var(--brand-gold); font-family: "Open Sans", sans-serif; font-size: 8px;
    letter-spacing: 1.8px; text-align: center; line-height: 17px;
  }

  .brand { position: absolute; display: flex; align-items: flex-start; gap: 6px; }
  .brand-dot { width: 14px; height: 14px; border-radius: 50%; background: var(--brand-blue); margin-top: 3px; }
  .brand-name { font-size: 17px; line-height: 19px; color: var(--brand-blue); letter-spacing: .5px; }
  .brand-tagline { font-family: "Open Sans", sans-serif; font-size: 7.5px; color: var(--brand-gold); margin-top: 2px; }

  /* Letterhead */
  .letterhead { left: 59px; top: 66px; width: 527px; height: 742px; }
  .letterhead .brand { left: 45px; top: 44px; }
  .contact { position: absolute; left: 350px; top: 45px; font-family: "Open Sans", sans-serif; font-size: 7.6px; color: var(--ink-dark); list-style: none; }
  .contact li { display: flex; gap: 5px; line-height: 11px; }
  .contact svg { width: 8px; height: 8px; flex: none; margin-top: 1.5px; fill: var(--brand-blue); }
  .letter-body { position: absolute; left: 45px; top: 206px; width: 438px; }
  .salutation { font-size: 13px; margin-bottom: 24px; color: var(--ink); }
  .letter-body p.para { font-size: 7.3px; line-height: 11.4px; margin-bottom: 11.5px; text-align: justify; }
  .closing { font-size: 7.3px; margin-top: 18px; }
  .signature { display: block; width: 62px; height: 24px; margin-top: 6px; background: linear-gradient(90deg, #e9e9ee, #dcdce4); }
  .letterhead .footer-band { top: 706px; }

  /* Envelope back */
  .envelope-back { left: 620px; top: 293px; width: 531px; height: 240px; }
  .flap { position: absolute; left: 0; top: 0; width: 531px; height: 80px; }
  .flap-mark { position: absolute; left: 0; right: 0; top: 28px; text-align: center; font-size: 9px; color: var(--brand-blue); letter-spacing: .5px; }

  /* Envelope front */
  .envelope-front { left: 620px; top: 566px; width: 533px; height: 242px; }
  .envelope-front .brand { left: 32px; top: 28px; }
  .return-address { position: absolute; left: 39px; top: 74px; font-family: "Open Sans", sans-serif; font-size: 7.8px; color: var(--ink-dark); }
  .envelope-front .footer-band { top: 205px; }
</style>
</head>
<body>

<section class="sheet letterhead">
  <div class="brand">
    <span class="brand-dot"></span>
    <div>
      <div class="brand-name">MARIAN T. HOLLOWAY</div>
      <div class="brand-tagline">Forensic Document Examiner</div>
    </div>
  </div>

  <ul class="contact">
    <li><svg viewBox="0 0 10 10"><path d="M2 0.5 L3.8 2.6 L2.9 3.8 C3.6 5.3 4.7 6.4 6.2 7.1 L7.4 6.2 L9.5 8 L8.4 9.5 C4.3 9.2 .8 5.7 .5 1.6 Z"/></svg><span>(555) 014-2290</span></li>
    <li><svg viewBox="0 0 10 10"><path d="M0.5 2 H9.5 V8.5 H0.5 Z M0.5 2 L5 5.5 L9.5 2" fill="none" stroke="#33309a" stroke-width="1.2"/></svg><span>mholloway@quillmarkreview.example</span></li>
    <li><svg viewBox="0 0 10 10"><path d="M5 0.3 C2.8 0.3 1.4 2 1.4 3.8 C1.4 6.2 5 9.7 5 9.7 C5 9.7 8.6 6.2 8.6 3.8 C8.6 2 7.2 0.3 5 0.3 Z M5 2.4 A1.4 1.4 0 1 1 5 5.2 A1.4 1.4 0 1 1 5 2.4 Z" fill-rule="evenodd"/></svg><span>P.O.Box 4120, Riverton,<br>OR 97000</span></li>
  </ul>

  <div class="letter-body">
    <p class="salutation">Dear Mr. Carter,</p>
    <p class="para">Lorem ipsum dolor sit amet, consectetur adipiscing elit. Donec orci purus, luctus vitae dignissim eu, iaculis sed purus. Vivamus faucibus, ipsum nec aliquet viverra, leo mauris condimentum ligula, sit amet sagittis enim ligula quis arcu. Nam egestas tortor id nisi porttitor mattis. In tortor ante, ultricies in suscipit a, tempus non massa. Vivamus et auctor mi. Fusce vel massa nulla. Phasellus nec eros mauris, et scelerisque orci.</p>
    <p class="para">Donec malesuada orci vitae nulla accumsan porta a id massa. Quisque accumsan iaculis magna sit amet fringilla. Maecenas consequat, magna eget tincidunt semper, odio nibh rutrum mi, id feugiat ante nisi eu risus. Vestibulum nunc orci, rhoncus a placerat in, ultricies in mi. Cras mattis varius eros, vel fringilla nisi suscipit eget. Quisque scelerisque sagittis nulla at porttitor.</p>
    <p class="para">Sed id augue vitae urna euismod commodo aliquet a quam. Pellentesque arcu velit, cursus et malesuada ut, consequat et diam. Nullam erat sem, rhoncus id ullamcorper vitae, rhoncus et arcu. In ultricies ultricies nulla, ut rutrum nisi iaculis at. Donec eu magna a metus ornare faucibus. Fusce aliquet faucibus ultricies. Morbi semper, est id tincidunt gravida, sem arcu adipiscing lacus, ac bibendum nulla leo eu purus. Quisque nec diam sed risus consectetur a ccumsan quis quis nibh. Vestibulum id purus lorem.</p>
    <p class="para">It is a long established fact that a reader will be distracted by the readable content of a page when looking at its layout. The point of using Lorem Ipsum is that it has a more-or-less normal distribution of letters, as opposed to using 'Content here, content here', making it look like readable English. Many desktop publishing packages</p>
    <p class="closing">Sincerely,</p>
    <span class="signature" role="img" aria-label="Handwritten signature"></span>
  </div>

  <div class="footer-band">www.quillmarkreview.example</div>
</section>

<section class="sheet envelope-back">
  <svg class="flap" viewBox="0 0 531 80" aria-hidden="true">
    <path d="M12 0 V50 Q12 71 36 71 H495 Q519 71 519 50 V0" fill="none" stroke="var(--fold)" stroke-width="2"/>
  </svg>
  <div class="flap-mark">MARIAN T. HOLLOWAY</div>
</section>

<section class="sheet envelope-front">
  <div class="brand">
    <span class="brand-dot"></span>
    <div>
      <div class="brand-name">MARIAN T. HOLLOWAY</div>
      <div class="brand-tagline">Forensic Document Examiner</div>
    </div>
  </div>
  <div class="return-address">P.O.Box 4120, Riverton, OR 97000</div>
  <div class="footer-band">www.quillmarkreview.example</div>
</section>

</body>
</html>
```